Occupational Therapist does home accessibility for disabled folks; needs business card design

We need a business card for a company in Portland, Oregon that specializes in making homes accessible, comfortable, and functional for people who are disabled or aging who would like to stay in THEIR home. Our medical background as Occupational Therapists allows us to translate the functional needs of the person into the recommendations for the design of the home remodel.

Target Market(s)

Elderly, children of elderly
People with disabilities, families of people with disabilities

Industry/Entity Type

Business

Contact Information for Business Card

Company name: HomeWell
Name: Karen Dwyer Lopez, OTR/L, CAPS, ECHM
Occupational Therapist, Home Modification & Accessibility Specialist
website: www.homewellsteady.com
email: homewellsteady@mailbright.com
phone: (503)418-2957
CCB #: 384517

Font styles to use
Sans Serif

Requirements
Must have
• My logo
• Easy to read font with contrasting background
• Please list the Services offered: Occupational Therapy, Home safety & accessibility assessments, Home modification consulting, project management
Nice to have
• Friendly, welcoming feel
Should not have
• Dark colored background

```html
<!DOCTYPE html>
<html lang="en">
<head>
<meta charset="utf-8">
<title>HomeWell Business Card</title>
<link rel="stylesheet" href="https://fonts.googleapis.com/css2?family=Jost:wght@400;500;600;700&display=swap">
<style>
  :root {
    --orange: #d17f2a;
    --grey: #6b6b6b;
    --grey-dark: #555657;
    --white: #ffffff;
    --stage: #e9e8e5;
  }
  * { box-sizing: border-box; margin: 0; padding: 0; }
  html, body {
    width: 1200px; height: 900px; overflow: hidden;
    background: var(--stage);
    font-family: "Jost", sans-serif;
  }
  .card {
    position: absolute; left: 280px;
    width: 640px; height: 365px;
    border-radius: 22px; overflow: hidden;
    box-shadow: 0 10px 28px rgba(0,0,0,.18);
  }
  .card-front { top: 70px; background: var(--orange); }
  .card-back { top: 465px; background: var(--white); }
  .card svg.shapes { position: absolute; inset: 0; }

  /* Front */
  .brand-name {
    position: absolute; font-weight: 500; letter-spacing: .5px;
    display: flex; align-items: center; gap: 12px;
  }
  .brand-name .mark { display: inline-block; }
  .card-front .brand-name {
    top: 48px; right: 40px; font-size: 58px; color: var(--white);
  }
  .card-front .brand-name .mark { width: 18px; height: 18px; background: var(--white); }
  .services {
    position: absolute; top: 150px; right: 36px;
    color: var(--white); font-size: 15.5px; text-align: right;
    line-height: 1.45; letter-spacing: .6px;
  }
  .services .sep { color: var(--grey-dark); padding: 0 4px; }
  .website {
    position: absolute; right: 36px; bottom: 40px;
    font-size: 15px; color: var(--grey-dark); letter-spacing: .4px;
  }
  .website strong { color: var(--orange); font-weight: 700; }

  /* Back */
  .card-back .brand-name {
    top: 150px; left: 42px; font-size: 46px; color: var(--orange);
  }
  .card-back .brand-name .mark { width: 16px; height: 16px; background: var(--orange); }
  .divider {
    position: absolute; left: 318px; top: 60px; width: 1px; height: 180px;
    background: linear-gradient(to bottom, transparent, var(--orange), transparent);
  }
  .contact {
    position: absolute; left: 338px; top: 58px; color: var(--grey);
    font-size: 14px; line-height: 1.35;
  }
  .contact .person { color: var(--orange); font-weight: 700; font-size: 21px; line-height: 1.2; }
  .contact .role { margin-bottom: 6px; }
  .contact ul { list-style: none; }
  .contact li { display: flex; align-items: center; gap: 8px; font-size: 14.5px; }
  .contact li svg { width: 12px; height: 12px; flex: none; }
  .contact .accent { color: var(--orange); }
  .licence {
    position: absolute; left: 34px; bottom: 20px;
    color: var(--white); font-size: 15px; letter-spacing: .6px;
  }
</style>
</head>
<body>

<section class="card card-front">
  <svg class="shapes" viewBox="0 0 640 365" width="640" height="365" aria-hidden="true">
    <path d="M0 338 C160 300 300 268 430 246 C310 280 160 318 0 356 Z" fill="var(--grey)"/>
    <path d="M0 365 L0 352 C190 312 420 258 640 232 L640 365 Z" fill="var(--white)"/>
  </svg>
  <div class="brand-name"><span class="mark"></span>HomeWell</div>
  <p class="services">
    Occupational Therapy<span class="sep">•</span>Home safety &amp; accessibility assessments<br>
    Home modification consulting<span class="sep">•</span>Project management
  </p>
  <p class="website">www.<strong>homewellsteady</strong>.com</p>
</section>

<section class="card card-back">
  <svg class="shapes" viewBox="0 0 640 365" width="640" height="365" aria-hidden="true">
    <path d="M360 286 C460 262 560 230 640 186 L640 200 C560 240 460 272 360 290 Z" fill="var(--grey)"/>
    <path d="M0 318 C220 306 450 264 640 204 L640 365 L0 365 Z" fill="var(--orange)"/>
  </svg>
  <div class="brand-name"><span class="mark"></span>HomeWell</div>
  <div class="divider"></div>
  <div class="contact">
    <p class="person">Karen Dwyer Lopez</p>
    <p class="role">OTR/L, CAPS, ECHM, Occupational Therapist<br>Home Modification &amp; Accessibility Specialist.</p>
    <ul>
      <li>
        <svg viewBox="0 0 12 12"><path d="M2.5 1 L4.5 1 L5.3 3.6 L4 4.6 C4.6 6 6 7.4 7.4 8 L8.4 6.7 L11 7.5 L11 9.5 C11 10.3 10.3 11 9.5 11 C5 11 1 7 1 2.5 C1 1.7 1.7 1 2.5 1 Z" fill="var(--orange)"/></svg>
        (503) 418-2957
      </li>
      <li>
        <svg viewBox="0 0 12 12"><rect x="1" y="2.5" width="10" height="7" fill="none" stroke="var(--orange)" stroke-width="1.3"/><path d="M1 3 L6 7 L11 3" fill="none" stroke="var(--orange)" stroke-width="1.3"/></svg>
        homewellsteady@mailbright.com
      </li>
      <li>
        <svg viewBox="0 0 12 12"><circle cx="6" cy="6" r="5" fill="none" stroke="var(--orange)" stroke-width="1.2"/><ellipse cx="6" cy="6" rx="2.2" ry="5" fill="none" stroke="var(--orange)" stroke-width="1"/><path d="M1 6 H11" stroke="var(--orange)" stroke-width="1"/></svg>
        www.<span class="accent">homewellsteady</span>.com
      </li>
    </ul>
  </div>
  <p class="licence">CCB #: 384517</p>
</section>

</body>
</html>
```